I need a website built for my modeling agency company.

On our website, a user can create a profile and we will submit it to thousands of modeling agents throughout the country.

In many cases, they will receive multiple offers from modeling agencies which allows them to pick and choose the contract that is best for them to launch their modeling career.

Some tag lines to consider using:

"Submit your profile to hundreds of modeling agents instantly!"

"Get found and become a star!"

We are: The Runway Guild.

Our Slogan: The World''s Largest Network of Fashion Models and Agents

What We Do: We are an agency with one of the largest networks of fashion professionals that are looking for new modeling talent. We host professional profiles for aspiring models, professional fashion models seeking work, modeling talent seekers, and top modeling agencies. We connect aspiring models with the top modeling agencies in the United States and abroad.

By submitting your FREE profile, you will be instantly introduced to the industry’s leading modeling agents. Within a few days, you could receive multiple, competing offers from modeling agencies that all want to launch your modeling career. Receiving multiple signing offers puts you in control of deciding which contract best suites you!

Reason: I've seen some good designs, but none that are 100% perfect. These are the ones that I like best so far (to give you some ideas): http://files.pixelvane.example/img/510372/820114/820114_4917263_510372_image.jpg http://files.pixelvane.example/img/510372/829305/829305_4926851_510372_image.jpg http://files.pixelvane.example/img/510372/51847/51847_4924097_510372_image.jpg http://files.pixelvane.example/img/510372/51847/51847_4919856_510372_image.jpg http://files.pixelvane.example/img/510372/823670/823670_4920438_510372_image.jpg

Target Market(s)

Aspiring models (mostly female, but some male)

Industry/Entity Type

Modeling Agency

Colors

Designer to choose colors to be used in the design.

Requirements
Nice to have
• Somewhere in the top half of the page, I would like there to be a small form for the visitor to fill out. This form will look as follows:

Title: Instantly contact hundreds of modeling agents who are looking for new talent and could make you a star!
Fields: First Name*, Last Name*, Age, Zip Code, Email Address*, Daytime Phone, Evening Phone, Comments.

Then, there will be a "submit" button to proceed to next step of form. Just below the "submit" button, should be the following verbiage: "You will have the opportunity to upload photo(s) and provide other pertinent information in next step."

```html
<!DOCTYPE html>
<html lang="en">
<head>
<meta charset="utf-8">
<title>The Runway Guild</title>
<link rel="stylesheet" href="https://fonts.googleapis.com/css2?family=Nunito:wght@300;400;700&display=swap">
<style>
:root{
  --canvas:#ececec;
  --page:#ffffff;
  --pink:#ef0a84;
  --pink-dark:#c5066c;
  --ink:#2e2e2e;
  --white:#ffffff;
}
*{box-sizing:border-box;margin:0;padding:0}
html,body{width:1200px;height:1000px;overflow:hidden}
body{background:var(--canvas);font-family:"Nunito",sans-serif;color:var(--ink);position:relative}
.page{position:absolute;left:148px;top:0;width:909px;height:1000px;background:var(--page);box-shadow:0 0 4px rgba(0,0,0,.35)}
.hero{position:absolute;left:0;top:0;width:909px;height:66px;background:linear-gradient(90deg,#3a3a3a 0%,#6d6d6d 30%,#9a9a9a 55%,#5a5a5a 80%,#2a2a2a 100%)}
.brand{position:absolute;left:138px;top:18px;display:flex;align-items:center;gap:8px;color:var(--white);font-size:17px;font-weight:400;letter-spacing:.5px}
.brand-mark{width:14px;height:14px;border-radius:50%;background:var(--white)}
.slider-dots{position:absolute;left:386px;top:37px;display:flex;gap:10px}
.slider-dots span{width:14px;height:14px;border-radius:50%;border:1.5px solid #bdbdbd}
.slider-dots span.active{background:var(--pink);border-color:#f3f3f3}
.credit{position:absolute;right:3px;top:41px;font-size:11.5px;color:#e6e6e6}
.steps{position:absolute;left:0;top:66px;width:909px;height:175px;background:var(--pink)}
.step{position:absolute;top:0;height:175px;width:182px;display:flex;align-items:center;justify-content:center;text-align:center;color:var(--white);font-size:19.5px;font-weight:300;line-height:23px;text-transform:uppercase}
.step.active{background:var(--pink-dark)}
.step-pointer{position:absolute;left:345px;top:241px}
.section-title{position:absolute;left:0;width:909px;text-align:center;color:var(--pink);font-size:19px;font-weight:700}
.section-text{position:absolute;left:0;width:909px;text-align:center;font-size:14.3px;line-height:20.5px;color:var(--ink)}
.section-text em{font-style:normal;color:var(--pink)}
.gallery{position:absolute;left:0;top:528px;width:909px;height:188px;display:flex;box-shadow:0 0 14px rgba(0,0,0,.3)}
.gallery div{height:188px}
.cta{position:absolute;left:383px;top:926px;width:136px;height:25px;background:var(--pink);color:var(--white);font-size:13px;font-weight:400;display:flex;align-items:center;justify-content:center;letter-spacing:.3px}
</style>
</head>
<body>
<main class="page">
  <header class="hero" role="img" aria-label="Black and white fashion photograph banner">
    <div class="brand"><span class="brand-mark"></span>The Runway Guild</div>
    <div class="slider-dots"><span></span><span></span><span class="active"></span></div>
    <div class="credit">This picture belongs to Marisol</div>
  </header>

  <nav class="steps">
    <div class="step" style="left:88px">Free<br>online<br>profile</div>
    <div class="step active" style="left:273px">Instantly<br>to fashion<br>world</div>
    <div class="step" style="left:455px">Lounch<br>modeling<br>career</div>
    <div class="step" style="left:633px">Become<br>a super<br>star</div>
  </nav>
  <svg class="step-pointer" width="46" height="23" viewBox="0 0 46 23"><polygon points="0,0 46,0 23,23" fill="#c5066c"/></svg>

  <h1 class="section-title" style="top:321px">Submit your profile to hundreds of modeling agents instantly!</h1>
  <p class="section-text" style="top:375px">By submitting your <em>FREE profile</em>, you will be instantly introduced to the industry’s <em>leading modeling</em><br><em>agents</em>. Within a few days, you could receive multiple, competing offers from modeling agencies<br>that all want to launch your <em>modeling career</em>. Receiving multiple signing offers puts you<br>in control of deciding which contract best suites you!</p>

  <section class="gallery">
    <div style="width:135px;background:linear-gradient(135deg,#6b3a2e,#c79a86 60%,#4a2620)" role="img" aria-label="Model portrait with auburn hair"></div>
    <div style="width:213px;background:linear-gradient(135deg,#d8d8d8,#8a8a8a 55%,#2f2f2f)" role="img" aria-label="Black and white model photograph"></div>
    <div style="width:213px;background:linear-gradient(135deg,#1e2430,#6a5a52 55%,#c9a58e)" role="img" aria-label="Glamour model photograph on dark background"></div>
    <div style="width:213px;background:linear-gradient(135deg,#ffffff,#e8c4ad 50%,#8a5a44)" role="img" aria-label="Beauty model photograph on white"></div>
    <div style="width:135px;background:linear-gradient(135deg,#6b4a3e,#c8a596 55%,#9a2a2e)" role="img" aria-label="Model portrait with red fabric"></div>
  </section>

  <h2 class="section-title" style="top:782px">The World''s Largest Network of Fashion Models and Agents</h2>
  <p class="section-text" style="top:837px">By submitting your <em>FREE profile</em>, you will be instantly introduced to the industry’s<br><em>leading modeling agents</em>. Within a few days, you could receive multiple,</p>

  <a class="cta">BE THE ONE</a>
</main>
</body>
</html>
```